TK Fiscal Website Redesign Contest

We want to refresh our website to be more insitutional, professional for an international audience. We have designed a new logo for this purpose and that has been attached. A full brand brief and positioning statement has also been attached. Please read through all the documents carefully before designing. The old website is found here: https://tk-fiscal-example.com/

Target Market(s)

Actuaries and associated businesses internationally

Industry/Entity Type

professional services - actuaries

Number of Pages Required

3 page

Font styles to use
Sans Serif

Colors
0054AA
0677BA
7BADD7
CADEEF
E8F1F8
0094D4
00A9DD
6FCCEA
C7EBF8
E9F6FB
F0912C
F2A743
F7CA91
FBE8D2
FDF5EE
EE7325
F08F49
F5BC92
FAE3D3
FDF4ED
EB3D1F
EC4F4E
F09395
F8D3D4
FCEDEE

Requirements
Must have
• blues and greens to match the logo color, complimentary colors, navigation
Nice to have
• old site: https://tk-fiscal-example.com/

```html
<!DOCTYPE html>
<html lang="en">
<head>
<meta charset="utf-8">
<title>TK Fiscal — Actuarial Software</title>
<link href="https://fonts.googleapis.com/css2?family=Lexend:wght@400;500;600;700&family=Figtree:wght@400;500;600;700&display=swap" rel="stylesheet">
<style>
:root{
  --primary:#0054AA;
  --primary-mid:#0677BA;
  --accent:#0094D4;
  --accent-bright:#00A9DD;
  --green:#1C9C78;
  --green-soft:#E3F4EE;
  --accent-soft:#E9F6FB;
  --ring:#CADEEF;
  --ring-line:#7BADD7;
  --ink:#111114;
  --text:#2b2b30;
  --muted:#55555c;
  --line:#d8d8dd;
  --panel:#F2F7FB;
  --footer:#06182E;
  --white:#ffffff;
}
*{margin:0;padding:0;box-sizing:border-box}
html,body{width:1200px;height:3831px;overflow:hidden}
body{position:relative;background:var(--white);font-family:"Figtree",sans-serif;color:var(--text)}
.abs{position:absolute}
h1,h2,h3,.heading{font-family:"Lexend",sans-serif;color:var(--ink)}
.btn{position:absolute;display:flex;align-items:center;justify-content:center;border-radius:30px;font-family:"Figtree",sans-serif;font-weight:600;font-size:12.5px;letter-spacing:.2px;color:var(--white);text-decoration:none;text-transform:uppercase;white-space:nowrap}
.btn-accent{background:var(--accent)}
.btn-primary{background:var(--primary)}
.btn-outline{border:1.5px solid rgba(255,255,255,.85)}
.eyebrow{position:absolute;left:0;width:1200px;text-align:center;color:var(--accent);font-size:17px;font-weight:500;text-transform:uppercase}
.section-title{position:absolute;left:0;width:1200px;text-align:center;font-size:34px;font-weight:600}

/* header */
.site-header{position:absolute;left:0;top:0;width:1200px;height:100px;background:var(--white)}
.brand{position:absolute;display:flex;align-items:center;gap:10px;font-family:"Lexend",sans-serif;font-weight:600;color:var(--ink);letter-spacing:1px;white-space:nowrap}
.brand-dot{width:14px;height:14px;border-radius:50%;background:var(--accent)}
.nav{position:absolute;left:315px;top:41px;display:flex;gap:17px;font-size:13px;color:var(--text);white-space:nowrap}

/* hero */
.hero{position:absolute;left:0;top:100px;width:1200px;height:578px;background:linear-gradient(135deg,#5b6472 0%,#2e3540 45%,#1d232c 100%)}
.hero-title{position:absolute;left:0;top:172px;width:1200px;text-align:center;color:var(--white);font-size:45px;font-weight:600;line-height:50px}
.hero-sub{position:absolute;left:0;top:286px;width:1200px;text-align:center;color:var(--white);font-size:17px;line-height:25px;font-family:"Lexend",sans-serif;font-weight:400}
.scroll-cue{position:absolute;left:559px;top:636px;width:82px;height:82px;border-radius:50%;background:var(--white);box-shadow:0 6px 20px rgba(0,0,0,.12);display:flex;align-items:center;justify-content:center}

/* pillars */
.pillar{position:absolute;top:862px;width:216px;height:256px;background:var(--white);border-radius:12px;box-shadow:0 6px 18px rgba(0,0,0,.07);padding:0 16px}
.pillar-icon{position:absolute;left:20px;top:20px;width:62px;height:66px;border-radius:46% 54% 50% 50%;background:var(--accent-soft);display:flex;align-items:center;justify-content:center}
.pillar h3{position:absolute;left:16px;top:102px;width:190px;font-size:15px;font-weight:600;line-height:23px}
.pillar p{position:absolute;left:16px;top:156px;width:190px;font-size:11px;line-height:19px;color:var(--muted)}

/* solutions */
.solutions{position:absolute;left:0;top:1193px;width:1200px;height:606px;background:var(--panel)}
.solutions-photo{position:absolute;left:599px;top:19px;width:601px;height:587px;background:linear-gradient(120deg,#3c4b5c 0%,#6c5a44 45%,#c6a172 70%,#e7d5ba 100%)}
.solution{position:absolute;left:141px;width:420px;height:74px}
.solution-icon{position:absolute;left:0;top:0;width:74px;height:74px;border-radius:50%;display:flex;align-items:center;justify-content:center}
.solution h3{position:absolute;left:88px;top:4px;font-size:15.5px;font-weight:500}
.solution p{position:absolute;left:88px;top:28px;width:330px;font-size:11px;line-height:19px;color:var(--text)}

/* characteristics */
.hub-ring{position:absolute;left:454px;top:1988px;width:292px;height:292px;border-radius:50%;background:var(--ring)}
.hub-core{position:absolute;left:484px;top:2018px;width:232px;height:232px;border-radius:50%;background:var(--white);display:flex;align-items:center;justify-content:center;font-family:"Lexend",sans-serif;font-weight:600;font-size:34px;color:var(--primary)}
.trait-icon{position:absolute;width:72px;height:72px;border-radius:50%;display:flex;align-items:center;justify-content:center}
.trait{position:absolute;width:240px}
.trait h3{font-size:15.5px;font-weight:500}
.trait p{font-size:11.5px;margin-top:4px;color:var(--text)}
.trait.left{text-align:right}

/* insights */
.feature-card{position:absolute;left:141px;top:2550px;width:531px;height:339px;border-radius:12px;background:linear-gradient(160deg,#6d7580 0%,#3b434d 50%,#1f252d 100%);overflow:hidden}
.feature-card .meta{position:absolute;left:30px;top:215px;color:var(--white);font-size:11px;display:flex;gap:6px;align-items:center}
.feature-card h3{position:absolute;left:30px;top:238px;color:var(--white);font-size:16.5px;font-weight:500}
.feature-card a{position:absolute;left:30px;top:273px;color:var(--white);font-size:10.5px;font-weight:600;text-decoration:underline}
.post{position:absolute;left:718px;width:350px}
.post .meta{font-size:10.5px;color:var(--muted);display:flex;gap:6px;align-items:center}
.post h3{margin-top:13px;font-size:14.5px;font-weight:500;line-height:19px;white-space:nowrap}
.post a{display:block;margin-top:10px;font-size:10.5px;font-weight:600;color:var(--ink);text-decoration:underline}
.post-rule{position:absolute;left:718px;width:338px;height:1.5px;background:var(--line)}

/* cta + footer */
.footer{position:absolute;left:0;top:3268px;width:1200px;height:563px;background:var(--footer)}
.cta{position:absolute;left:137px;top:3056px;width:926px;height:357px;border-radius:34px;background:radial-gradient(ellipse at 70% 30%,#00A9DD 0%,#0677BA 45%,#0054AA 100%);overflow:hidden}
.cta h2{position:absolute;left:0;top:68px;width:926px;text-align:center;color:var(--white);font-size:43px;font-weight:500;line-height:44px}
.cta p{position:absolute;left:0;top:165px;width:926px;text-align:center;color:var(--white);font-size:17px;line-height:25px;font-family:"Lexend",sans-serif}
.footer-col h4{font-family:"Lexend",sans-serif;color:var(--white);font-size:17px;font-weight:500}
.footer-col{position:absolute;top:3482px;color:var(--white);font-size:12.5px}
.footer-col ul{list-style:none;margin-top:14px}
.footer-col li{margin-bottom:12px}
.contact-item{display:flex;gap:12px;margin-top:14px;line-height:19px}
.social{display:flex;align-items:center;gap:12px;margin-top:14px}
.social-dot{width:28px;height:28px;border-radius:50%;border:1.5px solid var(--white);display:flex;align-items:center;justify-content:center}
.social-dot.active{background:var(--accent);border-color:var(--accent)}
.social-dot span{width:8px;height:8px;border-radius:50%;background:var(--white)}
.newsletter{position:absolute;left:141px;top:3619px;width:262px;height:32px;background:var(--white);border-radius:16px;display:flex;align-items:center;padding-left:14px;gap:8px;font-size:11px;color:var(--muted)}
.newsletter-go{position:absolute;right:4px;top:4px;width:24px;height:24px;border-radius:50%;background:var(--green);display:flex;align-items:center;justify-content:center}
.footer-rule{position:absolute;left:141px;top:3737px;width:990px;height:1px;background:#1f3552}
.copyright{position:absolute;left:0;top:3757px;width:1200px;text-align:center;color:var(--white);font-size:11.5px}
</style>
</head>
<body>

<header class="site-header">
  <div class="brand" style="left:42px;top:34px;font-size:24px;"><span class="brand-dot"></span>TK FISCAL</div>
  <nav class="nav"><span>PLATFORM</span><span>SOLUTIONS</span><span>INSIGHTS</span><span>COMPANY</span><span>CONTACT</span></nav>
  <a class="btn btn-accent" style="left:715px;top:28px;width:286px;height:42px;">Request a Technical Walkthrough</a>
  <a class="btn btn-primary" style="left:1011px;top:28px;width:128px;height:42px;">Client Login</a>
</header>

<section class="hero" role="img" aria-label="Photo of analysts reviewing financial charts with a calculator on a desk">
  <h1 class="hero-title">Actuarial Software For Structured,<br>Auditable Financial Analysis.</h1>
  <p class="hero-sub">TK Fiscal Develops Software That Translates Established Actuarial<br>Methodologies Into Disciplined, Decision-Ready Tools</p>
  <a class="btn btn-accent" style="left:448px;top:353px;width:303px;height:50px;">Request a Technical Walkthrough</a>
</section>
<div class="scroll-cue">
  <svg width="20" height="36" viewBox="0 0 20 36"><path d="M10 2v30M3 25l7 8 7-8" fill="none" stroke="#111" stroke-width="1.8"/></svg>
</div>

<p class="eyebrow" style="top:765px;">Our Four Pillars</p>
<h2 class="section-title" style="top:793px;">One Platform, Four Pillars</h2>

<div class="pillar" style="left:141px;">
  <div class="pillar-icon"><svg width="30" height="30" viewBox="0 0 30 30" fill="none" stroke="#0094D4" stroke-width="1.6"><circle cx="15" cy="11" r="6"/><path d="M5 27v-5h20v5M11 17l-3 5M19 17l3 5"/></svg></div>
  <h3>Structured<br>Workflows</h3>
  <p>Standardized processes that reduce errors and enforce consistency across teams and regions.</p>
</div>
<div class="pillar" style="left:364px;">
  <div class="pillar-icon"><svg width="30" height="30" viewBox="0 0 30 30" fill="none" stroke="#0094D4" stroke-width="1.6"><rect x="7" y="4" width="16" height="22" rx="2"/><circle cx="15" cy="14" r="4"/><path d="M11 21h8"/></svg></div>
  <h3>Transparency of<br>Assumptions</h3>
  <p>Every input, parameter and scenario is visible, documented and version-controlled.</p>
</div>
<div class="pillar" style="left:599px;">
  <div class="pillar-icon"><svg width="30" height="30" viewBox="0 0 30 30" fill="none" stroke="#0094D4" stroke-width="1.6"><circle cx="15" cy="15" r="9"/><circle cx="15" cy="15" r="4"/><path d="M15 3v4M15 23v4M3 15h4M23 15h4"/></svg></div>
  <h3>Auditability</h3>
  <p>End-to-end traceability with full audit trails designed for internal and regulatory reviews.</p>
</div>
<div class="pillar" style="left:842px;">
  <div class="pillar-icon"><svg width="30" height="30" viewBox="0 0 30 30" fill="none" stroke="#0094D4" stroke-width="1.6"><path d="M4 12l11-7 11 7M6 12v12M12 12v12M18 12v12M24 12v12M3 26h24"/></svg></div>
  <h3>Governance</h3>
  <p>Built-in controls, role-based access and approval flows to meet global compliance.</p>
</div>

<section class="solutions">
  <p class="abs" style="left:141px;top:91px;color:var(--accent);font-size:17px;font-weight:500;">POWERFUL</p>
  <h2 class="abs" style="left:141px;top:117px;font-size:34px;font-weight:600;">Core Solutions</h2>
  <p class="abs" style="left:141px;top:165px;font-size:15px;line-height:25px;">Modular applications that integrate seamlessly<br>– or work standalone.</p>

  <div class="solution" style="top:232px;">
    <div class="solution-icon" style="background:var(--primary);"><svg width="36" height="36" viewBox="0 0 36 36" fill="none" stroke="#fff" stroke-width="1.6"><path d="M6 30h24M9 30V20M15 30V16M21 30V22M27 30V12M8 16l7-6 6 5 8-8"/></svg></div>
    <h3>Reserving &amp; Valuation</h3>
    <p>Multi-jurisdictional valuation (IFRS 17, GAAP, SII)<br>with transparent, audit-ready calculations.</p>
  </div>
  <div class="solution" style="top:336px;">
    <div class="solution-icon" style="background:var(--green);"><svg width="36" height="36" viewBox="0 0 36 36" fill="none" stroke="#fff" stroke-width="1.6"><path d="M18 6l4 10h-8zM10 30h16M12 30l2-12M24 30l-2-12M6 14l4 2M30 14l-4 2"/></svg></div>
    <h3>Pricing</h3>
    <p>Advanced models for product pricing, scenario testing,<br>and assumption tuning to optimise profitability.</p>
  </div>
  <div class="solution" style="top:440px;">
    <div class="solution-icon" style="background:var(--accent);"><svg width="36" height="36" viewBox="0 0 36 36" fill="none" stroke="#fff" stroke-width="1.6"><circle cx="15" cy="15" r="8"/><path d="M15 23v8M11 31h8M24 10h6v10h-6"/></svg></div>
    <h3>Enterprise Risk Management</h3>
    <p>Holistic ERM with stress testing, capital modelling, and<br>governance across the entire organisation.</p>
  </div>

  <div class="solutions-photo" role="img" aria-label="Photo of a hand stopping a falling row of wooden dominoes"></div>
</section>

<p class="eyebrow" style="top:1887px;">Key Platform</p>
<h2 class="section-title" style="top:1915px;">Key Platform Characteristics</h2>

<svg class="abs" style="left:0;top:1990px;" width="1200" height="280" viewBox="0 0 1200 280" fill="none" stroke="#7BADD7" stroke-width="1.2" stroke-dasharray="2 4">
  <path d="M432 50h20l18 20"/><path d="M432 237h20l18-20"/><path d="M768 50h-20l-18 20"/><path d="M768 237h-20l-18-20"/>
</svg>
<div class="hub-ring"></div>
<div class="hub-core">TK Fiscal</div>

<div class="trait left" style="left:101px;top:2020px;"><h3>Transparent Assumptions</h3><p>Full visibility &amp; documentation</p></div>
<div class="trait-icon" style="left:360px;top:2004px;background:var(--accent);"><svg width="34" height="34" viewBox="0 0 34 34" fill="none" stroke="#fff" stroke-width="1.6"><rect x="5" y="8" width="24" height="16" rx="2"/><circle cx="13" cy="16" r="4"/><path d="M20 14h6M20 18h6M12 28l4-4 4 4"/></svg></div>

<div class="trait left" style="left:101px;top:2207px;"><h3>Comparative Analysis</h3><p>Full visibility &amp; documentation</p></div>
<div class="trait-icon" style="left:360px;top:2191px;background:var(--primary);"><svg width="34" height="34" viewBox="0 0 34 34" fill="none" stroke="#fff" stroke-width="1.6"><path d="M6 28h22M9 28V18M14 28V12M19 28V20"/><circle cx="23" cy="17" r="5"/><path d="M27 21l3 4"/></svg></div>

<div class="trait-icon" style="left:767px;top:2004px;background:var(--primary);"><svg width="34" height="34" viewBox="0 0 34 34" fill="none" stroke="#fff" stroke-width="1.6"><path d="M17 5a12 12 0 0 1 12 12M17 29A12 12 0 0 1 5 17"/><rect x="12" y="12" width="10" height="10"/><path d="M26 14l3 3 3-3M8 20l-3-3-3 3"/></svg></div>
<div class="trait" style="left:856px;top:2020px;"><h3>Structured Workflows</h3><p>End-to-end process automation</p></div>

<div class="trait-icon" style="left:767px;top:2191px;background:var(--green);"><svg width="34" height="34" viewBox="0 0 34 34" fill="none" stroke="#fff" stroke-width="1.6"><circle cx="17" cy="17" r="11"/><path d="M6 17h22M17 6c-5 6-5 16 0 22M17 6c5 6 5 16 0 22"/></svg></div>
<div class="trait" style="left:856px;top:2207px;"><h3>Multi-Jurisdictional</h3><p>Compliant across global regimes</p></div>

<p class="eyebrow" style="top:2460px;">News &amp; Updates</p>
<h2 class="section-title" style="top:2489px;">Latest Insights</h2>

<article class="feature-card" role="img" aria-label="Photo of a hand with a pen over financial figures and a city skyline">
  <div class="meta"><svg width="12" height="12" viewBox="0 0 12 12" fill="none" stroke="#fff" stroke-width="1.2"><rect x="1" y="2" width="10" height="9" rx="1"/><path d="M1 5h10M4 1v2M8 1v2"/></svg>16 Mar 2026</div>
  <h3>Advancements In Actuarial Methods For IFRS 17</h3>
  <a>READ MORE</a>
</article>

<article class="post" style="top:2550px;">
  <div class="meta"><svg width="12" height="12" viewBox="0 0 12 12" fill="none" stroke="#555" stroke-width="1.2"><rect x="1" y="2" width="10" height="9" rx="1"/><path d="M1 5h10M4 1v2M8 1v2"/></svg>16 Mar 2026</div>
  <h3>Governance In Multi-Jurisdictional Practice</h3>
  <a>READ MORE</a>
</article>
<div class="post-rule" style="top:2653px;"></div>
<article class="post" style="top:2671px;">
  <div class="meta"><svg width="12" height="12" viewBox="0 0 12 12" fill="none" stroke="#555" stroke-width="1.2"><rect x="1" y="2" width="10" height="9" rx="1"/><path d="M1 5h10M4 1v2M8 1v2"/></svg>16 Mar 2026</div>
  <h3>Building Audit-Ready Actuarial Models</h3>
  <a>READ MORE</a>
</article>
<div class="post-rule" style="top:2773px;"></div>
<article class="post" style="top:2791px;">
  <div class="meta"><svg width="12" height="12" viewBox="0 0 12 12" fill="none" stroke="#555" stroke-width="1.2"><rect x="1" y="2" width="10" height="9" rx="1"/><path d="M1 5h10M4 1v2M8 1v2"/></svg>16 Mar 2026</div>
  <h3>Sustainable Insurance In Africa: Insights From<br>The 49th AFRIA Conference</h3>
  <a>READ MORE</a>
</article>
<div class="post-rule" style="top:2894px;"></div>

<a class="btn btn-primary" style="left:519px;top:2922px;width:162px;height:42px;">Read All Insights</a>

<footer class="footer"></footer>

<section class="cta">
  <h2>Ready To See<br>TK Fiscal In Action?</h2>
  <p>Schedule A Personalized Technical Walkthrough And Discover How Our<br>Platform Can Transform Your Actuarial Processes.</p>
  <a class="btn btn-outline" style="left:311px;top:236px;width:303px;height:48px;">Request a Technical Walkthrough</a>
</section>

<div class="brand" style="left:144px;top:3510px;font-size:24px;color:var(--white);"><span class="brand-dot"></span>TK FISCAL</div>
<p class="abs" style="left:141px;top:3558px;color:var(--white);font-size:11px;line-height:19px;">Latest Updates, Exclusive Content, And Special<br>Offers? Subscribe To Our Newsletter!</p>
<div class="newsletter">
  <svg width="13" height="11" viewBox="0 0 13 11" fill="none" stroke="#0094D4" stroke-width="1.2"><rect x="1" y="1" width="11" height="9" rx="1"/><path d="M1 2l5.5 4L12 2"/></svg>Your Email
  <span class="newsletter-go"><svg width="10" height="10" viewBox="0 0 10 10" fill="none" stroke="#fff" stroke-width="1.4"><path d="M2 8l6-6M3 2h5v5"/></svg></span>
</div>

<div class="footer-col" style="left:476px;">
  <h4>Quick Links</h4>
  <ul><li>Company</li><li>Platform</li><li>Solutions</li><li>Insights</li><li>Contact</li></ul>
</div>

<div class="footer-col" style="left:669px;">
  <h4>Contact Details</h4>
  <div class="contact-item"><svg width="14" height="16" viewBox="0 0 14 16" fill="#fff"><path d="M7 0a6 6 0 0 0-6 6c0 4.5 6 10 6 10s6-5.5 6-10a6 6 0 0 0-6-6zm0 8.5A2.5 2.5 0 1 1 7 3.5a2.5 2.5 0 0 1 0 5z"/></svg><span>410 Harbor Crest Ave,<br>Suite 210<br>Maple Point, FL 33990</span></div>
  <div class="contact-item"><svg width="14" height="14" viewBox="0 0 14 14" fill="#fff"><path d="M3 0l2.5 3.5-1.5 2a8 8 0 0 0 4.5 4.5l2-1.5L14 11l-1.5 2.5C7 14 0 7 .5 1.5z"/></svg><span>Phone<br>+1(555)010-2048</span></div>
  <div class="contact-item"><svg width="14" height="11" viewBox="0 0 14 11" fill="none" stroke="#fff" stroke-width="1.4"><rect x="1" y="1" width="12" height="9"/><path d="M1 1l6 5 6-5"/></svg><span>Email<br>contact@tk-fiscal-example.com</span></div>
</div>

<div class="footer-col" style="left:923px;">
  <h4>Social Media</h4>
  <div class="social"><span class="social-dot active"><span></span></span>Friendspace</div>
  <div class="social"><span class="social-dot"><span></span></span>Vidstream</div>
  <div class="social"><span class="social-dot"><span></span></span>Worknet</div>
  <div class="social"><span class="social-dot"><span></span></span>Snapgrid</div>
</div>

<div class="footer-rule"></div>
<p class="copyright">© 2026 TK-Fiscal. All Rights Reserved. &nbsp;&nbsp;|&nbsp;&nbsp; Legal</p>

</body>
</html>
```